Velmoran Tabletop Deck Company (southern african focus for now) needs a e-commerce website

We need a website design for a playing card company based in Southern Africa/United States. We make locally-sourced playing cards (standard 52 card deck, with customized fronts and backs) for everyone and collaborate with local artists to uplift their talents, while celebrating their nation's culture, heritage, beauty and identity. We would like to see designs that use the colours blue (see flag of Eswatini as starting product), white and some red accents (or your recommendation). The final design should communicate elegance, fun and sustainable prosperity.

Target Market(s)

Everyone loves playing cards. From the solo adventurer to the party host, first time learner or expert, young, middle and old, we need to attract a broad audience that appreciates the finer things and supports sustainable, environmentally contentiousness causes that support the local economy and uplift local talent - thing global, act local.

Number of Pages Required

4 page

Font styles to use
Serif
Sans Serif

Requirements
Must have
• Pages to include Home (Main), About (Our Story), Shop and Contact
Nice to have
• While designs may be static, elements of graceful movement would be desirable. Perhaps functionality of scrolling down on homepage showing playing cards in use, front and back. Quindle and Zorbix store's capture that elegant yet rich look.
Should not have
• Too many products. We focus on 1-2.

```html
<!DOCTYPE html>
<html lang="en">
<head>
<meta charset="utf-8">
<title>Shop | Velmoran Tabletop Deck Company</title>
<link href="https://fonts.googleapis.com/css2?family=Montserrat:wght@300;400;500;600;700&family=Playfair+Display:wght@700&display=swap" rel="stylesheet">
<style>
:root{
  --white:#ffffff;
  --ink:#222222;
  --muted:#777777;
  --blue:#3b5bb5;
  --frame:#8e97cc;
  --red:#b51a1a;
  --band-top:#f2f2f2;
  --band-bottom:#bcbcbc;
  --footer-bar:#4a4a4a;
  --badge:#111111;
}
*{box-sizing:border-box;margin:0;padding:0}
html,body{width:759px;height:1200px;overflow:hidden;background:var(--white)}
body{position:relative;font-family:"Montserrat",sans-serif;color:var(--ink)}
.abs{position:absolute}
/* header */
.site-header{left:0;top:0;width:759px;height:26px;display:flex;align-items:center;padding:0 20px}
.brand{font-family:"Playfair Display",serif;font-weight:700;font-size:15px;color:var(--ink);display:flex;align-items:center;gap:4px}
.brand-dot{width:6px;height:6px;border-radius:50%;background:var(--ink)}
.main-nav{position:absolute;left:365px;top:8px;display:flex;gap:22px;font-size:9px}
.main-nav .active{border-bottom:1px solid var(--ink)}
.cart{position:absolute;left:600px;top:7px}
.locale{position:absolute;left:648px;top:7px;display:flex;align-items:center;gap:4px;font-size:7px}
.flag{width:16px;height:10px;background:linear-gradient(#3e5eb9 0 25%,#ffd900 25% 30%,#b10c0c 30% 70%,#ffd900 70% 75%,#3e5eb9 75%)}
.page-title{left:0;width:759px;top:80px;text-align:center;font-size:20px;font-weight:400;letter-spacing:1px}
/* newest */
.newest{left:0;top:157px;width:759px;height:218px;background:linear-gradient(var(--band-top),var(--band-bottom))}
.newest h2{position:absolute;left:0;width:759px;top:26px;text-align:center;font-size:14px;font-weight:500}
.pack-img{border-radius:2px}
.pack-cultural{background:linear-gradient(135deg,#6b3b28,#c6542b 40%,#2d4f9e 75%,#b51a1a)}
.pack-classic{background:linear-gradient(135deg,#4a3a30,#9a8a7a 50%,#3a2c24)}
.product-info{width:120px;font-size:6px;color:var(--muted);line-height:1.5}
.product-info h3{font-size:9px;color:var(--ink);font-weight:500;text-align:center;margin-bottom:5px}
.price{font-size:7px;text-align:center;margin:6px 0}
.price s{color:var(--muted);margin-right:6px}
.price strong{color:var(--ink)}
.btn{display:block;margin:0 auto;width:70px;height:16px;line-height:16px;text-align:center;font-size:6px;font-weight:600;color:var(--white);border-radius:2px}
.btn-blue{background:var(--blue)}
.btn-red{background:var(--red)}
/* feature panels */
.feature{left:18px;width:721px;height:273px;border:2px solid var(--frame)}
.feature-title{font-size:12px;font-weight:500}
.video{background:linear-gradient(135deg,#c9c9cc,#8a8a90 60%,#d8d8da);}
.video-warm{background:linear-gradient(135deg,#6b5a3e,#c44a26 45%,#3a3a6a 70%,#7a6a50)}
.bullets{font-size:6px;color:var(--ink);line-height:2;padding-left:10px}
.big-price{font-size:11px;font-weight:600}
.big-price s{font-size:8px;color:var(--muted);font-weight:400;margin-right:10px}
/* footer */
.footer-hero{left:0;top:1000px;width:759px;height:83px;background:linear-gradient(90deg,#e9dcdc,#f4eeee 40%,#d8c4c6 70%,#efe6e6)}
.footer-brand{position:absolute;left:0;width:759px;top:22px;text-align:center;font-family:"Playfair Display",serif;font-size:32px;font-weight:700;color:var(--ink)}
.footer-col{top:1088px;width:140px;text-align:center;font-size:7px;line-height:1.9}
.footer-col h4{font-size:10px;font-weight:500;margin-bottom:2px}
.social{display:flex;justify-content:center;gap:8px;margin-top:3px}
.social span{width:8px;height:8px;border-radius:50%;background:var(--ink)}
.store-badge{display:block;width:52px;height:15px;background:var(--badge);border-radius:3px;margin:4px auto 0}
.footer-bar{left:0;top:1174px;width:759px;height:26px;background:var(--footer-bar);color:#ddd;font-size:5px;display:flex;align-items:center;justify-content:space-between;padding:0 12px}
</style>
</head>
<body>

<header class="site-header abs">
  <div class="brand"><span class="brand-dot"></span>Velmoran</div>
  <nav class="main-nav"><span>Home</span><span>About</span><span class="active">Shop</span><span>Contact</span></nav>
  <svg class="cart" width="12" height="11" viewBox="0 0 12 11"><path d="M0 1h2l2 6h6l1.5-4.5H3" fill="none" stroke="#222" stroke-width="1.3"/><circle cx="4.5" cy="9.5" r="1" fill="#222"/><circle cx="9.5" cy="9.5" r="1" fill="#222"/></svg>
  <div class="locale"><span class="flag"></span><span>Eswatini ▾</span></div>
</header>

<h1 class="page-title abs">Shop</h1>

<section class="newest abs">
  <h2>Newest Packs</h2>
  <div class="pack-img pack-cultural abs" style="left:157px;top:76px;width:42px;height:100px" role="img" aria-label="Cultural Pack playing card box"></div>
  <div class="product-info abs" style="left:218px;top:78px">
    <h3>Cultural Pack</h3>
    <p>Lorem ipsum dolor sit amet consectetur adipiscing elit sed do eiusmod tempor</p>
    <p class="price"><s>49.95</s><strong>40.95</strong></p>
    <span class="btn btn-blue">Add to Cart</span>
  </div>
  <div class="pack-img pack-classic abs" style="left:405px;top:76px;width:45px;height:100px" role="img" aria-label="Classic Pack playing card box"></div>
  <div class="product-info abs" style="left:470px;top:78px">
    <h3>Classic Pack</h3>
    <p>Lorem ipsum dolor sit amet consectetur adipiscing elit sed do eiusmod tempor</p>
    <p class="price"><s>49.95</s><strong>40.95</strong></p>
    <span class="btn btn-blue">Add to Cart</span>
  </div>
</section>

<section class="feature abs" style="top:397px">
  <div class="pack-img pack-classic abs" style="left:70px;top:32px;width:58px;height:100px" role="img" aria-label="Classic Pack box with fanned cards"></div>
  <div class="product-info abs" style="left:140px;top:50px">
    <h3>Classic Pack</h3>
    <p>Lorem ipsum dolor sit amet consectetur adipiscing elit sed do eiusmod tempor</p>
  </div>
  <ul class="bullets abs" style="left:60px;top:140px">
    <li>Lorem ipsum dolor sit amet, consectetur</li>
    <li>Lorem ipsum dolor sit amet, consectetur</li>
    <li>Lorem ipsum dolor sit amet, consectetur</li>
  </ul>
  <p class="big-price abs" style="left:298px;top:194px"><s>49.95</s>40.95</p>
  <span class="btn btn-red abs" style="left:297px;top:222px">Add to Cart</span>
  <p class="feature-title abs" style="left:518px;top:36px">Video</p>
  <div class="video abs" style="left:425px;top:58px;width:290px;height:105px" role="img" aria-label="Video of a hand dealing a classic playing card"></div>
</section>

<section class="feature abs" style="top:696px">
  <p class="feature-title abs" style="left:130px;top:36px">Video</p>
  <div class="video-warm abs" style="left:66px;top:56px;width:283px;height:108px" role="img" aria-label="Video of a hand holding the Cultural Pack"></div>
  <div class="pack-img pack-cultural abs" style="left:500px;top:20px;width:58px;height:94px" role="img" aria-label="Cultural Pack box with fanned cards"></div>
  <div class="product-info abs" style="left:575px;top:30px">
    <h3>Cultural Pack</h3>
    <p>Lorem ipsum dolor sit amet consectetur adipiscing elit sed do eiusmod tempor</p>
  </div>
  <ul class="bullets abs" style="left:490px;top:125px">
    <li>Lorem ipsum dolor sit amet, consectetur</li>
    <li>Lorem ipsum dolor sit amet, consectetur</li>
    <li>Lorem ipsum dolor sit amet, consectetur</li>
  </ul>
  <p class="big-price abs" style="left:306px;top:194px"><s>49.95</s>40.95</p>
  <span class="btn btn-red abs" style="left:305px;top:220px">Add to Cart</span>
</section>

<footer>
  <div class="footer-hero abs" role="img" aria-label="Playing cards scattered on a table">
    <div class="footer-brand">Velmoran</div>
  </div>
  <div class="footer-col abs" style="left:118px">
    <h4>Links</h4>
    <p>Home</p><p>About</p><p>Shop</p><p>Contact</p>
  </div>
  <div class="footer-col abs" style="left:310px">
    <h4>Contact</h4>
    <div class="social"><span></span><span></span></div>
    <div class="social"><span></span><span></span></div>
  </div>
  <div class="footer-col abs" style="left:515px">
    <h4>Download App</h4>
    <span class="store-badge" role="img" aria-label="Quindle store badge"></span>
    <span class="store-badge" role="img" aria-label="Zorbix store badge"></span>
  </div>
  <div class="footer-bar abs">
    <span>© Velmoran 2020. All rights reserved.</span>
    <span>Terms · Privacy</span>
    <span></span>
  </div>
</footer>

</body>
</html>
```